Tebrolu - 13 different skin care oil bottle label designs

We need label designs for our private label Tebrolu.
The labels should be designed in Adobe Illustator. Please use warm or lightening colours. We like colours. But they should have a uniform look. It is necessary to show the fruit/trees/nuts. On the back label we will have description text in four languages, a barcode, Made in France, an adress.
We will use oval clear/transparent bottles. The label size for 150 ml is 50 x 90 mm. Label size for 250 ml bottles is 60 x 115 mm.
Argan Oil 150 ml 100% PURE
Avocado Oil 150 ml 100% PURE
Castor Oil 150 ml 100% PURE
Jojoba's Oil 150 ml 100% PURE
Apricot Oil 150 ml 100% PURE
Coconut Oil 150 ml 100% PURE
Macadamia's Oil 150 ml 100% PURE
Neem Oil 150 ml 100% PURE
Almond Oil 150 ml 100% PURE
Wheat germ Oil 150 ml 100% PURE
Pure Glycerine 250 ml
Pure Glycerine + rose water 250 ml
Parafin Oil 250 ml

```html
<!DOCTYPE html>
<html lang="en">
<head>
<meta charset="utf-8">
<title>Tebrolu oil labels</title>
<link rel="stylesheet" href="https://fonts.googleapis.com/css2?family=Baloo+2:wght@500;800&family=Open+Sans:wght@700&display=swap">
<style>
  :root {
    --macadamia: #6b1a10;
    --macadamia-a: #8a4a35;
    --macadamia-b: #4a2018;
    --neem: #7ff22e;
    --neem-a: #8fe05a;
    --neem-b: #4fae2a;
    --almond: #b5391a;
    --almond-a: #c8774d;
    --almond-b: #8a3a22;
    --wheat: #c07a35;
    --wheat-a: #d8a070;
    --wheat-b: #a5683a;
    --brand: #a8d23a;
    --paper: #ffffff;
  }
  html, body { margin: 0; padding: 0; overflow: hidden; background: var(--paper); }
  .sheet { position: relative; width: 1200px; height: 1183px; overflow: hidden; }
  .label { position: absolute; width: 300px; height: 534px; }
  .label--macadamia { left: 88px; top: 13px; }
  .label--neem { left: 447px; top: 13px; }
  .label--almond { left: 787px; top: 13px; }
  .label--wheat { left: 88px; top: 603px; }
  .brand-name { font-family: "Baloo 2", sans-serif; font-weight: 500; font-size: 19px; fill: var(--brand); }
  .product-name { font-family: "Baloo 2", sans-serif; font-weight: 800; font-size: 44px; }
  .volume { font-family: "Open Sans", sans-serif; font-weight: 700; font-size: 20px; fill: var(--paper); }
  .pure-tag { font-family: "Open Sans", sans-serif; font-weight: 700; font-size: 8px; fill: var(--paper); }
</style>
</head>
<body>
<main class="sheet">

  <!-- Macadamia -->
  <svg class="label label--macadamia" viewBox="0 0 300 534">
    <defs>
      <clipPath id="oval-mac"><ellipse cx="150" cy="267" rx="146" ry="263"/></clipPath>
      <radialGradient id="photo-mac" cx="0.55" cy="0.65" r="0.7">
        <stop offset="0" stop-color="#d9a860"/><stop offset="0.35" stop-color="var(--macadamia-a)"/><stop offset="1" stop-color="var(--macadamia-b)"/>
      </radialGradient>
    </defs>
    <g clip-path="url(#oval-mac)">
      <rect width="300" height="534" fill="var(--paper)"/>
      <path role="img" aria-label="Photo of macadamia nuts, one cracked open" d="M0 285 Q150 342 300 285 L300 534 L0 534Z" fill="url(#photo-mac)"/>
      <path d="M0 266 Q150 326 300 266 L300 285 Q150 342 0 285Z" fill="var(--macadamia)"/>
    </g>
    <ellipse cx="150" cy="267" rx="146" ry="263" fill="none" stroke="var(--macadamia)" stroke-width="3"/>
    <circle cx="150" cy="64" r="15" fill="var(--brand)"/>
    <text class="brand-name" x="150" y="108" text-anchor="middle">tebrolu</text>
    <text class="product-name" x="150" y="207" text-anchor="middle" fill="var(--macadamia)">Macadamia's</text>
    <text class="product-name" x="150" y="248" text-anchor="middle" fill="var(--macadamia)">Oil</text>
    <g class="pure-badge">
      <circle cx="150" cy="305" r="34" fill="var(--macadamia)" stroke="var(--paper)" stroke-width="1.5"/>
      <path d="M150 286 C144 296 141 300 141 305 A9 9 0 0 0 159 305 C159 300 156 296 150 286Z" fill="none" stroke="var(--paper)" stroke-width="2"/>
      <circle cx="150" cy="305" r="4" fill="var(--paper)"/>
      <text class="pure-tag" x="150" y="327" text-anchor="middle" transform="rotate(-20 150 327)">100% Pure</text>
    </g>
    <text class="volume" x="150" y="485" text-anchor="middle">150ml</text>
  </svg>

  <!-- Neem -->
  <svg class="label label--neem" viewBox="0 0 300 534">
    <defs>
      <clipPath id="oval-neem"><ellipse cx="150" cy="267" rx="146" ry="263"/></clipPath>
      <radialGradient id="photo-neem" cx="0.5" cy="0.55" r="0.7">
        <stop offset="0" stop-color="#9be86a"/><stop offset="0.5" stop-color="var(--neem-a)"/><stop offset="1" stop-color="var(--neem-b)"/>
      </radialGradient>
    </defs>
    <g clip-path="url(#oval-neem)">
      <rect width="300" height="534" fill="var(--paper)"/>
      <path role="img" aria-label="Photo of green neem fruits" d="M0 285 Q150 342 300 285 L300 534 L0 534Z" fill="url(#photo-neem)"/>
      <path d="M0 266 Q150 326 300 266 L300 285 Q150 342 0 285Z" fill="var(--neem)"/>
    </g>
    <ellipse cx="150" cy="267" rx="146" ry="263" fill="none" stroke="var(--neem)" stroke-width="3"/>
    <circle cx="150" cy="64" r="15" fill="var(--brand)"/>
    <text class="brand-name" x="150" y="108" text-anchor="middle">tebrolu</text>
    <text class="product-name" x="145" y="238" text-anchor="middle" fill="var(--neem)">Neem Oil</text>
    <g class="pure-badge">
      <circle cx="150" cy="305" r="34" fill="var(--neem)" stroke="var(--paper)" stroke-width="1.5"/>
      <path d="M150 286 C144 296 141 300 141 305 A9 9 0 0 0 159 305 C159 300 156 296 150 286Z" fill="none" stroke="var(--paper)" stroke-width="2"/>
      <circle cx="150" cy="305" r="4" fill="var(--paper)"/>
      <text class="pure-tag" x="150" y="327" text-anchor="middle" transform="rotate(-20 150 327)">100% Pure</text>
    </g>
    <text class="volume" x="150" y="485" text-anchor="middle">150ml</text>
  </svg>

  <!-- Almond -->
  <svg class="label label--almond" viewBox="0 0 300 534">
    <defs>
      <clipPath id="oval-alm"><ellipse cx="150" cy="267" rx="146" ry="263"/></clipPath>
      <radialGradient id="photo-alm" cx="0.5" cy="0.55" r="0.7">
        <stop offset="0" stop-color="#d99068"/><stop offset="0.5" stop-color="var(--almond-a)"/><stop offset="1" stop-color="var(--almond-b)"/>
      </radialGradient>
    </defs>
    <g clip-path="url(#oval-alm)">
      <rect width="300" height="534" fill="var(--paper)"/>
      <path role="img" aria-label="Photo of shelled almonds" d="M0 285 Q150 342 300 285 L300 534 L0 534Z" fill="url(#photo-alm)"/>
      <path d="M0 266 Q150 326 300 266 L300 285 Q150 342 0 285Z" fill="var(--almond)"/>
    </g>
    <ellipse cx="150" cy="267" rx="146" ry="263" fill="none" stroke="var(--almond)" stroke-width="3"/>
    <circle cx="150" cy="64" r="15" fill="var(--brand)"/>
    <text class="brand-name" x="150" y="108" text-anchor="middle">tebrolu</text>
    <text class="product-name" x="147" y="238" text-anchor="middle" fill="var(--almond)">Almond Oil</text>
    <g class="pure-badge">
      <circle cx="150" cy="305" r="34" fill="var(--almond)" stroke="var(--paper)" stroke-width="1.5"/>
      <path d="M150 286 C144 296 141 300 141 305 A9 9 0 0 0 159 305 C159 300 156 296 150 286Z" fill="none" stroke="var(--paper)" stroke-width="2"/>
      <circle cx="150" cy="305" r="4" fill="var(--paper)"/>
      <text class="pure-tag" x="150" y="327" text-anchor="middle" transform="rotate(-20 150 327)">100% Pure</text>
    </g>
    <text class="volume" x="150" y="485" text-anchor="middle">150ml</text>
  </svg>

  <!-- Wheat germ -->
  <svg class="label label--wheat" viewBox="0 0 300 534">
    <defs>
      <clipPath id="oval-wht"><ellipse cx="150" cy="267" rx="146" ry="263"/></clipPath>
      <radialGradient id="photo-wht" cx="0.5" cy="0.6" r="0.7">
        <stop offset="0" stop-color="#e2b890"/><stop offset="0.5" stop-color="var(--wheat-a)"/><stop offset="1" stop-color="var(--wheat-b)"/>
      </radialGradient>
    </defs>
    <g clip-path="url(#oval-wht)">
      <rect width="300" height="534" fill="var(--paper)"/>
      <path role="img" aria-label="Photo of wheat grains" d="M0 285 Q150 342 300 285 L300 534 L0 534Z" fill="url(#photo-wht)"/>
      <path d="M0 266 Q150 326 300 266 L300 285 Q150 342 0 285Z" fill="var(--wheat)"/>
    </g>
    <ellipse cx="150" cy="267" rx="146" ry="263" fill="none" stroke="var(--wheat)" stroke-width="3"/>
    <circle cx="150" cy="64" r="15" fill="var(--brand)"/>
    <text class="brand-name" x="150" y="108" text-anchor="middle">tebrolu</text>
    <text class="product-name" x="152" y="200" text-anchor="middle" fill="var(--wheat)">Wheat germ</text>
    <text class="product-name" x="156" y="248" text-anchor="middle" fill="var(--wheat)">Oil</text>
    <g class="pure-badge">
      <circle cx="150" cy="305" r="34" fill="var(--wheat)" stroke="var(--paper)" stroke-width="1.5"/>
      <path d="M150 286 C144 296 141 300 141 305 A9 9 0 0 0 159 305 C159 300 156 296 150 286Z" fill="none" stroke="var(--paper)" stroke-width="2"/>
      <circle cx="150" cy="305" r="4" fill="var(--paper)"/>
      <text class="pure-tag" x="150" y="327" text-anchor="middle" transform="rotate(-20 150 327)">100% Pure</text>
    </g>
    <text class="volume" x="150" y="485" text-anchor="middle">150ml</text>
  </svg>

</main>
</body>
</html>
```